Broschüre für Spezialist für den Transfer von mobil eingeschränkten Personen
Zielgruppe
Wir sind Spezialist für den Transfer von mobil eingeschränkten Personen. Unsere Zielgruppe für dieses Projekt sind (öffentliche) Schwimmbäder, Planer und Architekten.
Aufgabenstellung
Es soll unsere aktuelle Broschüre neu aufgesetzt werden. Diese hat aktuell 12 Seiten. Es sollen aber noch zwei weitere Produkte hinzu kommen, so dass wir auf 14 Seiten kommen werden. Eventuell werden wir auch noch Zubehör mit rein nehmen, so dass wir dann auf 16 Seiten kommen. Die aktuelle Broschüre habe ich Ihnen angehängt. Texte und Bilder können für einen ersten Entwurf gerne übernommen werden.
Seite 1 - 12 sollen übernommen werden
Seite 13 o-dive4 (https://www.beckenhebetec.com/de/o-dive4-lift-fuer-schwimmbecken/)
Seite 14 o-dive5 (https://www.beckenhebetec.com/de/o-dive5-lifte-fuer-schwimmbecken/)

```html
<!DOCTYPE html>
<html lang="de">
<head>
<meta charset="utf-8">
<title>Broschüre Schwimmbadlifter – Umschlag</title>
<link href="https://fonts.googleapis.com/css2?family=Oswald:wght@300;400;600;700&family=Jost:wght@400;500&display=swap" rel="stylesheet">
<style>
  :root{
    --bg:#e4e5e7;
    --paper:#ffffff;
    --paper-grey:#eeeff0;
    --blue-light:#8fdcf0;
    --blue-mid:#3cc3ee;
    --blue:#1fa4e4;
    --blue-deep:#1e6fd4;
    --grey-badge:#8b8c8e;
    --ink:#1b1b1b;
    --ink-soft:#555;
    --accent:#d9262a;
    --photo-a:#8fa59b;
    --photo-b:#b9d9dc;
  }
  *{margin:0;padding:0;box-sizing:border-box}
  html,body{width:1200px;height:1200px;overflow:hidden;background:var(--bg)}
  .spread{position:absolute;left:50px;top:218px;width:1100px;height:764px;display:flex;gap:20px}
  .page{position:relative;width:540px;height:764px;background:var(--paper);overflow:hidden;box-shadow:0 6px 24px rgba(0,0,0,.12)}
  .page--back{background:linear-gradient(90deg,var(--paper) 0%,var(--paper-grey) 100%)}
  .shapes{position:absolute;inset:0}
  .programme{position:absolute;left:190px;top:230px;width:330px;font-family:"Oswald",sans-serif;font-size:17px;line-height:1.3;color:var(--ink)}
  .programme b{font-weight:700}
  .programme span{font-weight:400}
  .product-thumbs{position:absolute;left:190px;top:300px;display:flex;gap:12px}
  .thumb{width:102px;height:92px;border-radius:14px;background:linear-gradient(160deg,var(--photo-a),var(--photo-b) 60%,var(--blue-mid))}
  .thumb:nth-child(2){background:linear-gradient(160deg,#7a9a6a,#c9ccc6 60%,#a34a3a)}
  .legal{position:absolute;left:40px;top:470px;width:470px;font-family:"Jost",sans-serif;font-size:8.5px;line-height:1.45;color:var(--ink-soft)}
  .legal-row{display:flex;gap:16px;margin-bottom:12px;align-items:flex-start}
  .legal-icon{width:36px;flex:none}
  .ec-rep{display:flex;border:1px solid var(--ink-soft);font-size:6.5px;width:38px}
  .ec-rep span{flex:1;text-align:center;padding:2px 0}
  .ec-rep span+span{border-left:1px solid var(--ink-soft)}
  .disclaimer{margin-left:52px}
  .imprint{position:absolute;left:40px;bottom:48px;display:flex;align-items:center;gap:22px}
  .brand{display:flex;align-items:center;gap:6px;font-family:"Oswald",sans-serif;font-weight:700;font-size:30px;letter-spacing:1px;color:var(--ink)}
  .brand-square{width:12px;height:12px;background:var(--accent)}
  .imprint-text{font-family:"Jost",sans-serif;font-weight:500;font-size:9.5px;line-height:1.45;color:var(--ink)}
  .cover-photo{position:absolute;left:0;top:0;width:430px;height:470px;background:linear-gradient(170deg,#5f7a62 0%,#b9bfb8 30%,#d8cfc3 50%,var(--photo-b) 75%,#7fd0de 100%)}
  .headline-panel{position:absolute;left:150px;top:300px;width:360px;height:260px;background:linear-gradient(135deg,var(--blue-mid),var(--blue-deep));padding:58px 24px 0 28px;color:#fff;font-family:"Oswald",sans-serif;text-transform:uppercase}
  .headline-main{font-size:58px;font-weight:700;line-height:1;letter-spacing:1px}
  .headline-sub{font-size:25px;font-weight:600;line-height:1.15;margin-top:8px}
  .headline-sub2{font-size:18.5px;font-weight:600;line-height:1.2}
  .badge{position:absolute;left:30px;top:238px;width:124px;height:124px;border-radius:50%;background:var(--grey-badge);display:flex;align-items:center;justify-content:center;text-align:center;color:#fff;font-family:"Oswald",sans-serif;font-weight:700;font-size:17px;line-height:1.1;text-transform:uppercase}
  .tagline{position:absolute;left:150px;top:600px;font-family:"Oswald",sans-serif;font-weight:300;font-size:25px;color:var(--ink-soft)}
  .page--front .brand{position:absolute;right:40px;bottom:56px}
</style>
</head>
<body>
<main class="spread">

  <section class="page page--back" aria-label="Rückseite">
    <svg class="shapes" viewBox="0 0 540 764" aria-hidden="true">
      <polygon points="0,40 330,40 160,764 0,764" fill="var(--blue-light)" opacity=".55"/>
      <polygon points="0,120 240,60 0,560" fill="var(--blue-mid)" opacity=".6"/>
      <polygon points="0,200 540,140 0,430" fill="var(--blue-light)" opacity=".5"/>
      <polygon points="90,0 300,0 60,300" fill="var(--paper)" opacity=".7"/>
    </svg>
    <p class="programme"><b>Unser Programm:</b> <span>Prophylaxesysteme Patientenlifter Schwimmbadlifter Rehasysteme Transportsysteme</span></p>
    <div class="product-thumbs">
      <div class="thumb" role="img" aria-label="Foto: Schwimmbadlifter mit Person am Beckenrand"></div>
      <div class="thumb" role="img" aria-label="Foto: Schwimmbadlifter im Garten"></div>
      <div class="thumb" role="img" aria-label="Foto: Schwimmbadlifter am Pool"></div>
    </div>
    <div class="legal">
      <div class="legal-row">
        <svg class="legal-icon" viewBox="0 0 36 24" aria-hidden="true"><path d="M2 22V10l7 5V10l7 5V4h5v18z" fill="var(--ink)"/></svg>
        <p>Aquavent Lifttechnik, LLC / PO Box 100 / 200 Harbor Lane / Riverton, Oregon 97000 USA · Phone: 555-010-2231 / Fax: 555-010-4334 / www.aquavent-lift.example / Made in USA</p>
      </div>
      <div class="legal-row">
        <div class="legal-icon"><div class="ec-rep"><span>EC</span><span>REP</span></div></div>
        <p>EUREP B.V. / Kanaalweg 12 / 1000 AB Voorstad / The Netherlands · info@eurep-example.nl / www.eurep-example.nl</p>
      </div>
      <p class="disclaimer">Der Hersteller behält sich zu jeder Zeit das Recht zu technischen sowie gestalterischen Änderungen vor. Farben können aus drucktechnischen Gründen von den tatsächlichen Farben abweichen.</p>
    </div>
    <div class="imprint">
      <div class="brand"><span class="brand-square"></span>KLF</div>
      <p class="imprint-text">KLF Rehatechnik GmbH<br>Lindenweg 12 63000 Musterstadt | Tel. 0 12 34 / 5678 0</p>
    </div>
  </section>

  <section class="page page--front" aria-label="Titelseite">
    <div class="cover-photo" role="img" aria-label="Foto: weißer Schwimmbadlifter am Beckenrand eines Freibads"></div>
    <svg class="shapes" viewBox="0 0 540 764" aria-hidden="true">
      <polygon points="330,200 540,120 540,640" fill="var(--blue)" opacity=".45"/>
      <polygon points="420,60 540,420 380,560" fill="var(--blue-mid)" opacity=".35"/>
      <polygon points="540,430 540,620 400,620" fill="var(--blue-light)" opacity=".6"/>
    </svg>
    <div class="headline-panel">
      <div class="headline-main">Spezialist</div>
      <div class="headline-sub">für den Transfer von</div>
      <div class="headline-sub2">mobil eingeschränkten Personen</div>
    </div>
    <div class="badge">Kompakt<br>Mobil<br>Stark</div>
    <p class="tagline">Unsere Schwimmbadlifter können mehr!</p>
    <div class="brand"><span class="brand-square"></span>KLF</div>
  </section>

</main>
</body>
</html>
```